Pipelining Product Supply Company Needs New Stationery

We need new stationery (letter head, with compliments slips & business card) for our industry leading pipe lining supply company. basically we sell product to other plumbers to carry out pipe relining.

Im looking for something, fresh, professional, sleek and modern at the same time.

Ive attached a copy of the logo and also some guidelines to follow for colours and fonts etc.

Target Market(s)

Plumbers

Industry/Entity Type

Plumbing

Font styles to use
Sans Serif

Requirements
Must have
• The logo, space for ABN, Address, Phone Number, website and email.
Nice to have
• Stand out from the crowd. To look sleep and professional.
Should not have
• Any other colours apart from what is on the guidelines.

```html
<!DOCTYPE html>
<html lang="en">
<head>
<meta charset="utf-8">
<title>Keyline Pipelining Supplies – Letterhead</title>
<link href="https://fonts.googleapis.com/css2?family=Arimo:wght@400;700&display=swap" rel="stylesheet">
<style>
  :root{
    --bg:#d3ecc0;
    --paper:#ffffff;
    --green:#7cc242;
    --green-soft:#e6f2dd;
    --charcoal:#3a3a3a;
    --charcoal-dark:#262626;
    --ink:#1e1e1e;
    --muted:#6b6b6b;
  }
  *{box-sizing:border-box;margin:0;padding:0}
  html,body{width:1200px;height:784px;overflow:hidden;background:var(--bg)}
  body{font-family:"Arimo",Arial,sans-serif;position:relative}

  .letterhead{
    position:absolute;left:338px;top:22px;width:523px;height:740px;
    background:var(--paper);overflow:hidden;
    box-shadow:0 6px 18px rgba(60,90,40,.18);
  }

  /* header */
  .header-rule{position:absolute;left:0;top:14px;width:40px;height:4px;background:var(--green)}
  .brand{
    position:absolute;left:44px;top:8px;
    color:var(--green);font-weight:700;line-height:1;
  }
  .brand-name{display:block;font-size:30px;letter-spacing:1px}
  .brand-tag{display:block;font-size:10px;letter-spacing:2.4px;margin-top:4px}
  .header-bar{
    position:absolute;left:200px;right:0;top:52px;height:8px;
    background:linear-gradient(var(--charcoal),var(--charcoal-dark));
  }

  /* body copy */
  .letter-body{
    position:absolute;left:58px;right:58px;top:86px;
    font-size:9.2px;line-height:1.36;color:var(--ink);text-align:left;
  }
  .letter-body p{text-indent:22px;margin-bottom:11px}
  .signature{
    display:block;width:150px;height:40px;margin:20px 0 0 30px;
    background:linear-gradient(90deg,#f1f1f1,#e4e4e4);border-radius:3px;
  }

  /* footer */
  .footer-watermark{
    position:absolute;right:24px;bottom:36px;
    font-size:54px;font-weight:700;color:var(--green-soft);line-height:1;letter-spacing:2px;
  }
  .footer-rule{position:absolute;left:0;bottom:44px;width:400px;height:3px;background:var(--green)}
  .footer-contacts{
    position:absolute;left:8px;bottom:30px;display:flex;gap:10px;
    font-size:6.4px;color:var(--muted);white-space:nowrap;
  }
  .footer-contacts span::before{
    content:"";display:inline-block;width:5px;height:5px;border-radius:50%;
    background:var(--charcoal);margin-right:3px;vertical-align:-0.5px;
  }
  .footer-bar{
    position:absolute;left:0;bottom:14px;width:400px;height:9px;
    background:linear-gradient(var(--charcoal),var(--charcoal-dark));
  }
  .footer-web{
    position:absolute;right:0;bottom:0;width:124px;height:30px;
    background:linear-gradient(var(--charcoal),var(--charcoal-dark));
    color:#fff;font-size:10px;font-weight:700;
    display:flex;align-items:center;justify-content:center;
  }
</style>
</head>
<body>
  <main class="letterhead">
    <header>
      <div class="header-rule"></div>
      <div class="brand">
        <span class="brand-name">KEYLINE</span>
        <span class="brand-tag">PIPELINING SUPPLIES</span>
      </div>
      <div class="header-bar"></div>
    </header>

    <section class="letter-body">
      <p>Lorem ipsum dolor sit amet, consectetur adipiscing elit, sed do eiusmod tempor incididunt ut labore et dolore magna aliqua. Ut enim ad minim veniam, quis nostrud exercitation ullamco laboris nisi ut aliquip ex ea commodo consequat. Duis aute irure dolor in reprehenderit in voluptate velit esse cillum dolore eu fugiat nulla pariatur. Excepteur sint occaecat cupidatat non proident, sunt in culpa qui officia deserunt mollit anim id est laborum. Integer posuere erat a ante venenatis dapibus posuere velit aliquet lorem ipsum.</p>
      <p>Sed ut perspiciatis unde omnis iste natus error sit voluptatem accusantium doloremque laudantium, totam rem aperiam, eaque ipsa quae ab illo inventore veritatis et quasi architecto beatae vitae dicta sunt explicabo. Nemo enim ipsam voluptatem quia voluptas sit aspernatur aut odit aut fugit, sed quia consequuntur magni dolores eos qui ratione voluptatem sequi nesciunt. Neque porro quisquam est, qui dolorem ipsum quia dolor sit amet, consectetur, adipisci velit, sed quia non numquam eius modi tempora incidunt ut labore.</p>
      <p>Nam libero tempore, cum soluta nobis est eligendi optio cumque nihil impedit quo minus id quod maxime placeat facere possimus, omnis voluptas assumenda est, omnis dolor repellendus. Temporibus autem quibusdam et aut officiis debitis aut rerum necessitatibus saepe eveniet ut et voluptates repudiandae sint et molestiae non recusandae. Itaque earum rerum hic tenetur a sapiente delectus, ut aut reiciendis voluptatibus maiores alias consequatur aut perferendis doloribus asperiores repellat. Donec sed odio dui, cras mattis consectetur purus sit amet fermentum.</p>
      <span class="signature" role="img" aria-label="Handwritten signature of the sender"></span>
    </section>

    <footer>
      <div class="footer-watermark">KEYLINE</div>
      <div class="footer-rule"></div>
      <div class="footer-contacts">
        <span>00001 Example Avenue Suite 000, Australia, 00000</span>
        <span>(000) 000 0000</span>
        <span>hello@keylinepipe.com.au</span>
        <span>ABN 000000000</span>
      </div>
      <div class="footer-bar"></div>
      <div class="footer-web">www.keylinepipe.com.au</div>
    </footer>
  </main>
</body>
</html>
```